Ferncastle Financial - Website Design

We need a website design for a new commercial real estate company called Ferncastle Financial. We're effectively commercial mortgage brokers connecting real estate investors to lenders. We need a website that is simple (not busy), elegant, professional, and user-friendly. A lot of the users will be in their 50's and less tech savvy, so a stream-lined design is best. The website will serve as a portal for lenders to review new financing opportunities, as well as for real estate investors to review terms from lenders.
Updates
Just uploaded our logo.
Target Market(s)
Commercial real estate investors and lenders
Industry/Entity Type
Real Estate
Number of Pages Required
1 page
Colors
Designer to choose colors to be used in the design.
Look and feel

```html
<!DOCTYPE html>
<html lang="en">
<head>
<meta charset="utf-8">
<title>Ferncastle Financial</title>
<link href="https://fonts.googleapis.com/css2?family=Lato:wght@400;700;900&family=Oswald:wght@300;400&display=swap" rel="stylesheet">
<style>
:root{
  --brand:#2a2e9c;
  --brand-dark:#1f2280;
  --hero-a:#4a4fd8;
  --hero-b:#2b2fa8;
  --ink:#1c1c1c;
  --body:#444;
  --muted:#777;
  --line:#d9d9d9;
  --paper:#ffffff;
  --soft:#f3f3f3;
  --band:#1d1d1d;
  --icon:#555;
}
*{margin:0;padding:0;box-sizing:border-box}
html,body{width:1200px;height:3158px;overflow:hidden}
body{position:relative;font-family:'Lato',sans-serif;color:var(--body);background:var(--paper)}
.abs{position:absolute}

/* hero */
.hero{left:0;top:0;width:1200px;height:596px;background:linear-gradient(180deg,var(--hero-a),var(--hero-b) 60%,#3b3fb8)}
.hero-scene{left:330px;top:140px;width:620px;height:456px;background:linear-gradient(180deg,rgba(255,255,255,.08),rgba(255,255,255,.18));border-radius:4px 4px 0 0}
.topbar{left:0;top:0;width:1200px;height:50px;color:#fff;font-size:12px}
.social{left:50px;top:12px;display:flex;gap:14px}
.social span{width:24px;height:24px;border-radius:50%;background:rgba(255,255,255,.85)}
.contact-top{right:50px;top:16px;display:flex;gap:24px;align-items:center}
.contact-top div{display:flex;gap:8px;align-items:center}
.navbar{left:50px;top:53px;width:1100px;height:57px;background:var(--paper);display:flex;align-items:center;padding:0 18px}
.brand{font-family:'Lato',sans-serif;font-weight:700;font-size:26px;color:var(--brand)}
.menu{margin-left:auto;display:flex;gap:38px;font-size:14px;font-weight:700;color:#333}
.menu .on{color:var(--brand)}
.nav-sep{width:1px;height:26px;background:#999;margin:0 18px 0 26px}
.hero-title{left:0;top:205px;width:1200px;text-align:center;font-family:'Oswald',sans-serif;font-weight:300;font-size:76px;color:#fff;letter-spacing:1px}
.hero-sub{left:130px;top:290px;width:940px;text-align:center;font-size:28px;line-height:38px;color:#fff;font-weight:400}
.btn-ghost-light{left:524px;top:430px;width:124px;height:50px;border:2px solid #fff;color:#fff;font-size:18px;display:flex;align-items:center;justify-content:center;background:rgba(255,255,255,.12)}

/* headings */
.sec-title{left:0;width:1200px;text-align:center;font-weight:900;font-size:27px;color:var(--ink);text-transform:uppercase}
.rule{left:528px;width:144px;height:6px}
.rule i{position:absolute;top:2px;height:2px;background:#333}
.rule i:nth-child(1){left:0;width:46px}
.rule i:nth-child(2){left:54px;width:36px;top:0;height:6px;background:#222}
.rule i:nth-child(3){left:98px;width:46px}
.rule.light i{background:#ddd}

.intro{left:130px;top:700px;width:940px;text-align:center;font-size:15px;line-height:25px;color:#333}

/* service cards */
.card{top:768px;width:250px;height:327px;background:var(--paper);box-shadow:0 2px 12px rgba(0,0,0,.18);text-align:center}
.card svg{margin-top:36px}
.card h3{margin-top:20px;font-size:16px;font-weight:700;color:var(--ink);text-transform:uppercase}
.card p{margin:8px 22px 0;font-size:13px;line-height:17px;color:#555}
.btn{display:inline-flex;align-items:center;justify-content:center;font-size:12px}
.card .btn{margin-top:24px;width:88px;height:30px}
.btn-solid{background:var(--brand);color:#fff}
.btn-outline{border:1px solid #999;color:#777;background:#fff}

/* about */
.about-bg{left:0;top:1137px;width:1200px;height:750px;background:linear-gradient(90deg,#e9e9e9,#f4f4f4);clip-path:polygon(0 42px,1200px 0,1200px 700px,484px 740px,0 750px)}
.about-photo{left:0;top:1175px;width:480px;height:709px;background:linear-gradient(120deg,#c9ccd4,#7d8594 45%,#2f3542 75%,#aeb4bf)}
.about-title{left:484px;top:1326px;font-weight:900;font-size:27px;color:var(--ink);text-transform:uppercase}
.about-rule{left:540px;top:1370px}
.about-lead{left:476px;top:1390px;width:680px;font-size:22px;line-height:29px;color:#111}
.about-text{left:476px;top:1468px;width:682px;font-size:15.5px;line-height:25px;color:#555}
.about-btn{left:474px;top:1689px;width:110px;height:40px;font-size:15px}

/* blog */
.post{top:1993px;width:346px;height:480px;background:var(--paper);box-shadow:0 2px 12px rgba(0,0,0,.18)}
.post-meta{height:55px;display:flex;align-items:center;padding:0 20px;font-size:13px;color:#444}
.avatar{width:32px;height:32px;border-radius:50%;background:#8a8f99;margin-right:16px}
.post-meta .date{margin-left:auto;color:#666}
.post-img{height:212px}
.post h4{margin:16px 26px 0;font-size:14.5px;line-height:20px;color:var(--ink);font-weight:700}
.post p{margin:8px 26px 0;font-size:13px;line-height:19px;color:#666}
.post .btn{margin:22px 0 0 26px;width:110px;height:38px;font-size:13px}

/* testimonials */
.band{left:0;top:2523px;width:1200px;height:325px;background:linear-gradient(90deg,#151515,#2a2a2a 50%,#141414)}
.band .sec-title{color:#fff;top:40px}
.quote{top:2627px;width:380px;height:176px;background:var(--paper)}
.quote .mark{position:absolute;left:-6px;top:38px;width:26px;height:26px;background:var(--brand);color:#fff;font-size:24px;font-weight:900;line-height:30px;text-align:center}
.quote .face{position:absolute;left:28px;top:38px;width:104px;height:104px;border-radius:50%}
.quote .txt{position:absolute;left:150px;top:38px;width:215px}
.quote h5{font-size:17px;color:var(--ink);font-weight:700}
.quote .role{font-size:12px;color:#777;margin-top:6px}
.quote p{font-size:11.5px;line-height:16px;color:#666;margin-top:6px}

/* footer */
.footer{left:0;top:2848px;width:1200px;height:257px;background:#f6f6f6}
.fcol h6{font-size:17px;font-weight:700;color:var(--ink)}
.fcol .ul{width:92px;height:1px;background:#bbb;margin-top:10px}
.fcol p{font-size:12.5px;line-height:21px;color:#666;margin-top:12px}
.sub-input{width:226px;height:30px;background:#222;display:flex;align-items:center;gap:10px;padding-left:6px;color:#aaa;font-size:11px;margin-top:14px}
.sub-input b{width:30px;height:20px;background:#fff}
.sub-btn{width:90px;height:28px;margin-top:12px;font-size:12px}
.touch{font-size:12.5px;color:#333;line-height:19px}
.touch .row{display:flex;gap:10px;margin-top:14px}
.touch .name{font-weight:700}
.fsocial{display:flex;gap:16px;margin-top:16px}
.fsocial span{width:18px;height:18px;border-radius:50%;background:var(--brand)}
.bottombar{left:0;top:3105px;width:1200px;height:53px;background:var(--brand);color:#fff;font-size:13px;display:flex;align-items:center;padding:0 50px}
.bottombar nav{display:flex;gap:8px}
.bottombar .copy{margin-left:auto}
</style>
</head>
<body>

<!-- hero -->
<section class="abs hero">
  <div class="abs hero-scene" role="img" aria-label="Modern glass-fronted house at dusk under a blue tint"></div>
  <div class="abs topbar">
    <div class="abs social"><span></span><span></span><span></span><span></span><span></span></div>
    <div class="abs contact-top">
      <div><svg width="16" height="12" viewBox="0 0 16 12"><rect x="1" y="1" width="14" height="10" fill="none" stroke="#fff" stroke-width="1.5"/><path d="M1 1l7 6 7-6" fill="none" stroke="#fff" stroke-width="1.5"/></svg>info@ferncastlefin.example</div>
      <div><svg width="14" height="14" viewBox="0 0 14 14"><path d="M3 1l3 3-2 2c1 2 2 3 4 4l2-2 3 3-2 3C6 14 0 8 1 3z" fill="#fff"/></svg>123.456.7890</div>
    </div>
  </div>
  <header class="abs navbar">
    <div class="brand">Ferncastle Financial</div>
    <nav class="menu"><span class="on">HOME</span><span>ABOUT US</span><span>BROKERAGE</span><span>AGENTS</span><span>NEWS</span><span>BLOG</span><span>CONTACT</span></nav>
    <div class="nav-sep"></div>
    <svg width="22" height="22" viewBox="0 0 22 22"><circle cx="9" cy="9" r="7" fill="none" stroke="#333" stroke-width="2.5"/><path d="M14 14l6 6" stroke="#333" stroke-width="3"/></svg>
  </header>
  <h1 class="abs hero-title">FINANCIAL SERVICES</h1>
  <p class="abs hero-sub">We are commercial real estate company called Ferncastle Financial. We're effectively commercial mortgage brokers connecting real estate investors to lenders.</p>
  <div class="abs btn-ghost-light">Read More</div>
</section>

<!-- services -->
<h2 class="abs sec-title" style="top:636px">How can an financial help you?</h2>
<div class="abs rule" style="top:681px"><i></i><i></i><i></i></div>
<p class="abs intro">Objectively innovate empowered manufactured products whereas parallel platforms. Holisticly predominate extensible testing procedures for reliable supply chains. Dramatically engage top-line web services vis-a-vis cutting-edge deliverables.</p>

<div class="abs card" style="left:50px">
  <svg width="80" height="80" viewBox="0 0 80 80"><path d="M40 6L8 34h10v10L40 24l22 20V34h10z" fill="var(--brand)"/><path d="M4 46l14 4 10 12 12 6 12-6 10-12 14-4-8 18-18 12H30L12 64z" fill="var(--brand)"/></svg>
  <h3>Mortgage Brokers</h3>
  <p>Lorem ipsum dolor sit amet, ctetur adipiscing elit am sit amet posuere orci, ut convallis sem Vestibulum imperdiet sit ame</p>
  <span class="btn btn-solid">Read More</span>
</div>
<div class="abs card" style="left:328px">
  <svg width="80" height="80" viewBox="0 0 80 80"><path d="M40 8L12 32h8v22h40V32h8z" fill="var(--icon)"/><rect x="34" y="38" width="12" height="16" fill="#fff"/><path d="M10 58h24l12 6h14l8-6v12H10z" fill="var(--icon)"/></svg>
  <h3>Real Estate Investors</h3>
  <p>Lorem ipsum dolor sit amet, ctetur adipiscing elit am sit amet posuere orci, ut convallis sem Vestibulum imperdiet sit ame</p>
  <span class="btn btn-outline">Read More</span>
</div>
<div class="abs card" style="left:606px">
  <svg width="80" height="80" viewBox="0 0 80 80"><rect x="14" y="20" width="24" height="54" fill="var(--icon)"/><rect x="40" y="8" width="28" height="66" fill="var(--icon)"/><g fill="#fff"><rect x="20" y="28" width="5" height="6"/><rect x="28" y="28" width="5" height="6"/><rect x="20" y="40" width="5" height="6"/><rect x="28" y="40" width="5" height="6"/><rect x="46" y="16" width="6" height="6"/><rect x="56" y="16" width="6" height="6"/><rect x="46" y="28" width="6" height="6"/><rect x="56" y="28" width="6" height="6"/><rect x="46" y="40" width="6" height="6"/><rect x="56" y="40" width="6" height="6"/><rect x="50" y="60" width="8" height="14"/></g></svg>
  <h3>Real Estate Lenders</h3>
  <p>Lorem ipsum dolor sit amet, ctetur adipiscing elit am sit amet posuere orci, ut convallis sem Vestibulum imperdiet sit ame</p>
  <span class="btn btn-outline">Read More</span>
</div>
<div class="abs card" style="left:888px">
  <svg width="80" height="80" viewBox="0 0 80 80"><rect x="24" y="6" width="32" height="22" fill="var(--icon)"/><circle cx="40" cy="17" r="7" fill="#fff"/><text x="40" y="21" font-size="11" text-anchor="middle" fill="var(--icon)" font-family="Lato,sans-serif" font-weight="700">$</text><path d="M6 30l12 14 8 18h8V48L22 34zM74 30L62 44l-8 18h-8V48l12-14z" fill="var(--icon)"/></svg>
  <h3>Financial Services</h3>
  <p>Lorem ipsum dolor sit amet, ctetur adipiscing elit am sit amet posuere orci, ut convallis sem Vestibulum imperdiet sit ame</p>
  <span class="btn btn-outline">Read More</span>
</div>

<!-- about -->
<div class="abs about-bg"></div>
<div class="abs about-photo" role="img" aria-label="Two businessmen reviewing work at a laptop in an office"></div>
<h2 class="abs about-title">A fre details about Ferncastle Financial</h2>
<div class="abs rule about-rule"><i></i><i></i><i></i></div>
<p class="abs about-lead">Lorem ipsum dolor sit amet, consectetur adipiscing elit.<br>Duis sed massa aliquam, elementum nisi congue, condimen velit.</p>
<p class="abs about-text">Nulla placerat libero laoreet, auctor turpis ac, mollis odio. Mauris condimentum fria lacinia. Curabitur feugiat egestas sollicitudin. Proin ante nibh, posuere sit amet urpis vel, consequat accumsan massa. Cras commodo erat nibh, quis ulvinar sem dapibus vitae. Cras non ipsum volutpat, dapibus orci sit amet, egestas metus. Pellentesque non magna id lorem semper eleifend. Nullam sagittis est non euismod elementum. Class aptent taciti sociosqu ad litora torquent per conubia nostra, per inceptos hios. Orci varius natoque penatibus et magnis dis parturient montes, nascetur ridiculus . Vivamus porttitor mauris nec lectus pharetra auctor.</p>
<span class="abs btn btn-solid about-btn">Read More</span>

<!-- blog -->
<h2 class="abs sec-title" style="top:1913px">Latest Blog</h2>
<div class="abs rule" style="top:1958px"><i></i><i></i><i></i></div>

<article class="abs post" style="left:50px">
  <div class="post-meta"><span class="avatar"></span>Admin<span class="date">13 Nov 2017</span></div>
  <div class="post-img" role="img" aria-label="City skyline lit up at night over the water" style="background:linear-gradient(180deg,#1c2230,#3a3f4e 55%,#6b5a3a 80%,#2a2a30)"></div>
  <h4>Lorem ipsum dolor sit amet, consecte Turadipiscing elit. Suspendisse facili</h4>
  <p>Lorem ipsum dolor sit amet, consectetur adipisg elitusipendisse facilisis dictum metus eget ntum. Nunc lacinia euismod enim sed</p>
  <span class="btn btn-solid">Read More</span>
</article>
<article class="abs post" style="left:421px">
  <div class="post-meta"><span class="avatar"></span>Admin<span class="date">14 Nov 2017</span></div>
  <div class="post-img" role="img" aria-label="Waterfront hotel towers at blue hour" style="background:linear-gradient(180deg,#1a5fc4,#2f7de0 50%,#0d3f8c 80%,#0a2c66)"></div>
  <h4>Lorem ipsum dolor sit amet, consecte Turadipiscing elit. Suspendisse facili</h4>
  <p>Lorem ipsum dolor sit amet, consectetur adipisg elitusipendisse facilisis dictum metus eget ntum. Nunc lacinia euismod enim sed</p>
  <span class="btn btn-outline">Read More</span>
</article>
<article class="abs post" style="left:791px">
  <div class="post-meta"><span class="avatar"></span>Admin<span class="date">15 Nov 2017</span></div>
  <div class="post-img" role="img" aria-label="Living room interior with red armchairs" style="background:linear-gradient(160deg,#d8cbb5,#a88a6a 45%,#9b3a2e 70%,#6a4a34)"></div>
  <h4>Lorem ipsum dolor sit amet, consecte Turadipiscing elit. Suspendisse facili</h4>
  <p>Lorem ipsum dolor sit amet, consectetur adipisg elitusipendisse facilisis dictum metus eget ntum. Nunc lacinia euismod enim sed</p>
  <span class="btn btn-outline">Read More</span>
</article>

<!-- testimonials -->
<section class="abs band">
  <h2 class="abs sec-title">What our customers are saying!!</h2>
  <div class="abs rule light" style="top:86px"><i></i><i></i><i></i></div>
</section>
<div class="abs quote" style="left:139px">
  <span class="mark">&ldquo;</span>
  <div class="face" role="img" aria-label="Portrait of a smiling customer" style="background:linear-gradient(135deg,#b07a52,#5a3524)"></div>
  <div class="txt"><h5>Vestibulum Odio</h5><div class="role">Nunc laciniaeuism</div><p>Phasellus feugiat sapien quis fermentum hendr. Donec consequat faucibusellus vitae ultrices. Praesent malesuada facilisis mi, id pretium ex</p></div>
</div>
<div class="abs quote" style="left:610px">
  <span class="mark">&ldquo;</span>
  <div class="face" role="img" aria-label="Portrait of a customer in a suit" style="background:linear-gradient(135deg,#c9ccd2,#2c3444)"></div>
  <div class="txt"><h5>Vestibulum Odio</h5><div class="role">Nunc laciniaeuism</div><p>Phasellus feugiat sapien quis fermentum hendr. Donec consequat faucibusellus vitae ultrices. Praesent malesuada facilisis mi, id pretium ex</p></div>
</div>

<!-- footer -->
<footer class="abs footer">
  <div class="abs fcol" style="left:50px;top:44px;width:350px">
    <h6>About Us</h6><div class="ul"></div>
    <p>Lorem ipsum dolor sit amet, consectetur adipiscing elit. Suspendisse facilisis dictum metus eget elementum. Nunc lacinia euismod enim sed malesuada. In maximus ante vel sapien consectetur, at facilisis elit lacinia. Sed eleifend sit amet dui accumsan suscipit. Nullam metus purus, pulvinar sit amet egestas nec, elementum ac velit. Pellentesque</p>
  </div>
  <div class="abs fcol" style="left:535px;top:44px;width:280px">
    <h6>Ferncastle Newsletters</h6>
    <p>Subscribe to keep up to date with Ferncastle financial news, updates, roster additions and just plain old good stuff!!!!</p>
    <div class="sub-input"><b></b>your@email.com</div>
    <span class="btn btn-solid sub-btn">Subscribe</span>
  </div>
  <div class="abs fcol touch" style="left:922px;top:44px;width:240px">
    <h6>Get In Touch</h6>
    <div class="row"><svg width="14" height="18" viewBox="0 0 14 18"><path d="M7 0a7 7 0 017 7c0 5-7 11-7 11S0 12 0 7a7 7 0 017-7z" fill="var(--brand)"/><circle cx="7" cy="7" r="2.5" fill="#fff"/></svg><div><div class="name">Ferncastle Financial</div>Lorem 9, Ispum doaf 8-12 amet Street Donec non leo NSW 123</div></div>
    <div class="row"><svg width="14" height="14" viewBox="0 0 14 14"><path d="M3 1l3 3-2 2c1 2 2 3 4 4l2-2 3 3-2 3C6 14 0 8 1 3z" fill="var(--brand)"/></svg>123 456 7890</div>
    <div class="row"><svg width="16" height="12" viewBox="0 0 16 12"><rect x="1" y="1" width="14" height="10" fill="var(--brand)"/><path d="M1 1l7 6 7-6" fill="none" stroke="#fff" stroke-width="1.3"/></svg>hello@ferncastle.example</div>
    <div class="fsocial"><span></span><span></span><span></span><span></span><span></span><span></span></div>
  </div>
</footer>
<div class="abs bottombar">
  <nav><span>Home</span>/<span>About Us</span>/<span>Brokerage</span>/<span>Agents</span>/<span>News</span>/<span>Blog</span>/<span>Contact Us</span></nav>
  <span class="copy">© 2017 Ferncastle Financial. All Rights Reserved.</span>
</div>

</body>
</html>
```